Project Title:
Dental Implant Overdenture Flyer (Retirement Village Target)
Objective:
Create a clean, trustworthy, and reassuring flyer aimed at older adults (60–85 years old) who struggle with loose dentures. The goal is to educate them about implant-retained “clip-on” dentures and encourage them to book a consultation.
Tone & Feel:
Warm, caring, non-intimidating
Premium but not “salesy”
Medical but easy to understand
Focus on improving quality of life (confidence, eating, comfort)
Target Audience:
Retirees / pensioners
Existing denture wearers
People frustrated with loose or uncomfortable dentures
Key Message:
“You don’t have to live with loose dentures anymore.”
Design Style:
Clean, minimal, modern
Soft colours (blues, greens, warm neutrals)
Easy-to-read large font
High contrast for older eyes
Avoid clutter
Imagery Suggestions:
Smiling older adults (natural, not stocky/overly staged)
Before/after lifestyle (eating, laughing, socialising)
Simple diagram showing denture clipping onto implants
Avoid graphic surgical images
Layout Suggestions:
A5 or DL flyer
Clear sections with headings
Icons for benefits
Strong call-to-action at bottom
HEADLINE (big and bold)
Tired of Loose Dentures?
Discover Secure “Clip-On” Teeth
🔹 PROBLEM SECTION
Do your dentures:
Slip or move when eating?
Make it hard to chew certain foods?
Feel uncomfortable or loose?
Affect your confidence when speaking or smiling?
You’re not alone — and there is a better solution.
🔹 SOLUTION SECTION
Implant-Retained “Clip-On” Dentures
We can secure your denture using just 2 dental implants, allowing your teeth to:
✔ Stay firmly in place
✔ Improve your ability to eat
✔ Feel more comfortable
✔ Boost your confidence
🔹 SIMPLE EXPLANATION (very important)
Small titanium implants are gently placed in the jaw.
Your denture then clips securely onto them, stopping movement.
🔹 PRICE SECTION (highlight this clearly)
$12,000
Includes:
2 dental implants
A brand new custom overdenture
Does not include sedation or extractions (if needed)
🔹 SEDATION
Sedation is available for comfort.
If you hold a pensioner card, you may receive a significant Vantrel rebate, often resulting in minimal out-of-pocket costs for sedation.
🔹 TRUST / REASSURANCE
Experienced implant clinician
Gentle, patient-focused care
Modern technology and techniques
🔹 CALL TO ACTION (VERY IMPORTANT)
Book a Free Consultation
📞 Call: 08 5127 3046
🌐 Visit: www.brolvenclinic.com.au
📍 Located near Tallowmere shopping centre
🔹 OPTIONAL TAGLINE
Eat Better. Feel Better. Smile with Confidence Again.
Please include some photos to illustrate what a clip on denture looks like with two implants.

```html
<!DOCTYPE html>
<html lang="en">
<head>
<meta charset="utf-8">
<title>Clip-On Dentures Flyer</title>
<link rel="stylesheet" href="https://fonts.googleapis.com/css2?family=Montserrat:wght@300;400;500;600;700;800;900&display=swap">
<style>
:root{
  --navy:#0f4f86;
  --navy-deep:#0d3d6b;
  --teal:#0f93a8;
  --teal-dark:#0b7c92;
  --red:#c8283a;
  --red-dark:#8e1623;
  --ink:#3b3f45;
  --line:#9aa7b3;
  --bg-top:#f1f9fd;
  --bg-bottom:#c3e3f8;
}
*{margin:0;padding:0;box-sizing:border-box}
html,body{width:851px;height:1200px;overflow:hidden}
body{font-family:'Montserrat',sans-serif;color:var(--ink)}
.flyer{position:relative;width:851px;height:1200px;overflow:hidden;
  background:linear-gradient(170deg,var(--bg-top) 0%,var(--bg-top) 55%,#e2f1fb 75%,var(--bg-bottom) 100%)}
.abs{position:absolute}
.brand{left:64px;top:45px;width:200px;height:87px;background:#fff;display:flex;align-items:center;gap:10px;padding:0 12px}
.brand-dot{width:22px;height:22px;border-radius:50%;background:var(--teal);flex:none}
.brand-name{font-weight:600;font-size:13px;line-height:1.25;color:var(--navy);letter-spacing:.5px}
.hl-1{left:95px;top:170px;font-size:50px;font-weight:400;color:var(--ink);line-height:1}
.hl-2{left:68px;top:208px;font-size:84px;font-weight:900;color:var(--navy);line-height:1;letter-spacing:-1px}
.hl-3{left:68px;top:283px;font-size:54px;font-weight:800;color:var(--navy);line-height:1}
.hl-sub{left:68px;top:339px;font-size:20.5px;font-weight:700;color:var(--ink)}
.hl-sub em{font-style:normal;color:var(--teal)}
.hero-photo{left:452px;top:74px;width:316px;height:284px;border-radius:0 0 158px 158px;
  background:radial-gradient(circle at 50% 42%,#f1dccb 0%,#ece2d8 45%,#eef5f9 85%)}
.hero-arc{left:410px;top:130px}
.card{border:1.2px solid var(--line);border-radius:0 14px 14px 0;border-left:none}
.tab{border-radius:20px 0 20px 0;color:#fff;font-weight:800;display:flex;align-items:center;justify-content:center}
.tab span{transform:rotate(-90deg);white-space:nowrap;letter-spacing:1px}
.tab-red{background:linear-gradient(180deg,var(--red-dark),var(--red))}
.tab-teal{background:linear-gradient(180deg,var(--teal-dark),var(--teal))}
.card-title{font-size:14.5px;font-weight:700;color:var(--navy);line-height:1.3;background:var(--bg-top);padding-right:8px}
.list{list-style:none}
.list li{display:flex;gap:6px;font-size:12.6px;line-height:1.25;margin-bottom:10.5px}
.list li b{font-weight:700}
.ico{flex:none;width:13px;height:13px;margin-top:1px}
.problems .list{left:119px;top:429px;width:285px}
.problems .note{left:120px;top:556px;font-size:12.6px;font-weight:600;line-height:1.35}
.solution .lead{left:481px;top:443px;font-size:12.6px;font-weight:500;line-height:1.3;width:300px}
.solution .list{left:486px;top:490px}
.diagram{left:90px;top:643px;width:275px;height:134px;border-radius:40px 40px 60px 60px;
  background:linear-gradient(180deg,#ffffff 0%,#eef1f3 50%,#f4b9bb 75%,#ee9ea4 100%)}
.explain{left:432px;top:638px;width:340px;font-size:15.2px;font-weight:800;color:var(--navy);line-height:1.28}
.rule{height:1.2px;background:var(--line)}
.sec-h{font-size:18px;font-weight:800;color:var(--navy);line-height:1.2}
.info-list{list-style:none;font-size:12.4px;line-height:1.4}
.info-list li{display:flex;gap:8px;margin-bottom:6px}
.price-box{left:69px;top:831px;width:340px;height:196px;border:1.2px solid var(--line);border-left:none;border-top:none;border-radius:0 0 12px 0}
.price-cap{left:376px;top:831px;width:33px;height:14px;border-top:1.2px solid var(--line);border-right:1.2px solid var(--line);border-radius:0 12px 0 0}
.price{left:120px;top:801px;font-size:66px;font-weight:900;color:var(--teal);line-height:1;letter-spacing:-2px}
.price sup{font-size:32px;vertical-align:top;position:relative;top:6px;margin-right:2px}
.incl-h{left:69px;top:891px;font-size:14px;font-weight:700;color:var(--navy)}
.incl{left:69px;top:919px;font-size:12.3px;font-weight:700}
.incl li{margin-bottom:3px}
.excl{left:69px;top:971px;font-size:12.3px;font-weight:700;color:var(--navy);line-height:1.35}
.clinician{left:672px;top:940px;width:179px;height:260px;
  clip-path:polygon(40px 0,179px 0,179px 100%,0 100%,0 150px,40px 110px);
  background:linear-gradient(180deg,rgba(233,205,180,.2) 0%,#e3c2a3 25%,#d9b595 45%,#2a2a2a 58%,#1c1c1c 100%)}
.cta{left:69px;top:1068px;width:607px;height:40px;border-radius:20px;background:linear-gradient(90deg,var(--navy-deep),var(--navy));display:flex;align-items:center}
.cta-label{color:#fff;font-size:24px;font-weight:800;padding-left:15px;width:345px;white-space:nowrap}
.cta-phone{height:40px;flex:1;background:#fff;border:2px solid var(--navy);border-radius:20px;display:flex;align-items:center;justify-content:center;gap:8px;font-size:25px;font-weight:800;color:var(--navy-deep);white-space:nowrap}
.footer{left:72px;top:1119px;font-size:15.6px;font-weight:600;color:var(--ink);white-space:nowrap}
.footer .sep{margin:0 10px}
</style>
</head>
<body>
<main class="flyer">
  <div class="abs brand"><span class="brand-dot"></span><span class="brand-name">BROLVEN IMPLANTS<br>DENTAL SURGERY</span></div>

  <h1>
    <span class="abs hl-1">Tired of</span>
    <span class="abs hl-2">Loose</span>
    <span class="abs hl-3">Dentures?</span>
  </h1>
  <p class="abs hl-sub">Discover Secure <em>“Clip-On”</em> Teeth</p>

  <div class="abs hero-photo" role="img" aria-label="Photo of a smiling senior couple"></div>
  <svg class="abs hero-arc" width="370" height="240" viewBox="0 0 370 240">
    <path d="M33 14 Q22 30 22 56 A173 173 0 0 0 368 56 Q368 30 357 14" fill="none" stroke="var(--teal)" stroke-width="4"/>
    <path d="M36 2 L20 30 L42 22 Z M354 2 L370 30 L348 22 Z" fill="var(--teal)"/>
  </svg>

  <section class="problems">
    <div class="abs tab tab-red" style="left:69px;top:402px;width:38px;height:204px"><span style="font-size:19px">PROBLEMS</span></div>
    <div class="abs card" style="left:107px;top:413px;width:302px;height:193px"></div>
    <h2 class="abs card-title" style="left:119px;top:397px">Do your dentures</h2>
    <ul class="abs list">
      <li><svg class="ico" viewBox="0 0 14 14"><circle cx="7" cy="7" r="7" fill="var(--red)"/><text x="7" y="10.5" font-size="10" font-weight="700" fill="#fff" text-anchor="middle" font-family="Montserrat,sans-serif">?</text></svg><span><b>Slip or move</b> when eating?</span></li>
      <li><svg class="ico" viewBox="0 0 14 14"><circle cx="7" cy="7" r="7" fill="var(--red)"/><text x="7" y="10.5" font-size="10" font-weight="700" fill="#fff" text-anchor="middle" font-family="Montserrat,sans-serif">?</text></svg><span>Make it <b>hard to chew</b> certain foods?</span></li>
      <li><svg class="ico" viewBox="0 0 14 14"><circle cx="7" cy="7" r="7" fill="var(--red)"/><text x="7" y="10.5" font-size="10" font-weight="700" fill="#fff" text-anchor="middle" font-family="Montserrat,sans-serif">?</text></svg><span>Feel <b>uncomfortable</b> or <b>loose</b>?</span></li>
      <li><svg class="ico" viewBox="0 0 14 14"><circle cx="7" cy="7" r="7" fill="var(--red)"/><text x="7" y="10.5" font-size="10" font-weight="700" fill="#fff" text-anchor="middle" font-family="Montserrat,sans-serif">?</text></svg><span><b>Affect your confidence</b> when<br>speaking or smiling?</span></li>
    </ul>
    <p class="abs note">You’re not alone — and there is<br>a better solution.</p>
  </section>

  <section class="solution">
    <div class="abs tab tab-teal" style="left:432px;top:402px;width:38px;height:204px"><span style="font-size:19px">SOLUTION</span></div>
    <div class="abs card" style="left:470px;top:413px;width:310px;height:193px"></div>
    <h2 class="abs card-title" style="left:480px;top:397px">Implant-Retained<br>“Clip-On” Dentures</h2>
    <p class="abs lead">We can secure your denture using just<br>2 dental implants, allowing your teeth to</p>
    <ul class="abs list">
      <li><svg class="ico" viewBox="0 0 14 14"><circle cx="7" cy="7" r="7" fill="var(--teal-dark)"/><path d="M3.8 7.2 L6.1 9.4 L10.3 4.9" fill="none" stroke="#fff" stroke-width="1.7"/></svg><span><b>Stay firmly</b> in place</span></li>
      <li><svg class="ico" viewBox="0 0 14 14"><circle cx="7" cy="7" r="7" fill="var(--teal-dark)"/><path d="M3.8 7.2 L6.1 9.4 L10.3 4.9" fill="none" stroke="#fff" stroke-width="1.7"/></svg><span><b>Improve</b> your <b>ability to eat</b></span></li>
      <li><svg class="ico" viewBox="0 0 14 14"><circle cx="7" cy="7" r="7" fill="var(--teal-dark)"/><path d="M3.8 7.2 L6.1 9.4 L10.3 4.9" fill="none" stroke="#fff" stroke-width="1.7"/></svg><span>Feel more <b>comfortable</b></span></li>
      <li><svg class="ico" viewBox="0 0 14 14"><circle cx="7" cy="7" r="7" fill="var(--teal-dark)"/><path d="M3.8 7.2 L6.1 9.4 L10.3 4.9" fill="none" stroke="#fff" stroke-width="1.7"/></svg><span>Boost your <b>confidence</b></span></li>
    </ul>
  </section>

  <div class="abs diagram" role="img" aria-label="Illustration of teeth in gum with a titanium implant post"></div>
  <p class="abs explain">Small titanium implants are gently placed in the jaw. Your denture then clips securely onto them, stopping movement.</p>

  <div class="abs rule" style="left:432px;top:736px;width:348px"></div>
  <section>
    <h2 class="abs sec-h" style="left:432px;top:754px">SEDATION</h2>
    <ul class="abs info-list" style="left:433px;top:787px;width:320px">
      <li><svg class="ico" viewBox="0 0 14 14"><circle cx="7" cy="7" r="7" fill="var(--teal-dark)"/><path d="M3.8 7.2 L6.1 9.4 L10.3 4.9" fill="none" stroke="#fff" stroke-width="1.7"/></svg><span>Sedation is available for comfort.</span></li>
      <li style="margin-top:8px"><svg class="ico" viewBox="0 0 14 14"><circle cx="7" cy="7" r="7" fill="var(--teal-dark)"/><path d="M3.8 7.2 L6.1 9.4 L10.3 4.9" fill="none" stroke="#fff" stroke-width="1.7"/></svg><span>If you hold a pensioner card, you may receive a significant Vantrel rebate, often resulting in minimal out-of-pocket costs for sedation.</span></li>
    </ul>
  </section>

  <div class="abs rule" style="left:432px;top:911px;width:348px"></div>
  <section>
    <h2 class="abs sec-h" style="left:433px;top:927px">TRUST / REASSURANCE</h2>
    <ul class="abs info-list" style="left:433px;top:963px">
      <li><svg class="ico" viewBox="0 0 14 14"><circle cx="7" cy="7" r="7" fill="var(--teal-dark)"/><path d="M3.8 7.2 L6.1 9.4 L10.3 4.9" fill="none" stroke="#fff" stroke-width="1.7"/></svg><span>Experienced implant clinician</span></li>
      <li><svg class="ico" viewBox="0 0 14 14"><circle cx="7" cy="7" r="7" fill="var(--teal-dark)"/><path d="M3.8 7.2 L6.1 9.4 L10.3 4.9" fill="none" stroke="#fff" stroke-width="1.7"/></svg><span>Gentle, patient-focused care</span></li>
      <li><svg class="ico" viewBox="0 0 14 14"><circle cx="7" cy="7" r="7" fill="var(--teal-dark)"/><path d="M3.8 7.2 L6.1 9.4 L10.3 4.9" fill="none" stroke="#fff" stroke-width="1.7"/></svg><span>Modern technology and techniques</span></li>
    </ul>
  </section>

  <section>
    <div class="abs price-box"></div>
    <div class="abs price-cap"></div>
    <div class="abs tab tab-red" style="left:69px;top:808px;width:38px;height:70px"><span style="font-size:14px">PRICE</span></div>
    <p class="abs price"><sup>$</sup>12,000</p>
    <h3 class="abs incl-h">Includes</h3>
    <ul class="abs info-list incl">
      <li><svg class="ico" viewBox="0 0 14 14"><circle cx="7" cy="7" r="7" fill="var(--teal-dark)"/><path d="M3.8 7.2 L6.1 9.4 L10.3 4.9" fill="none" stroke="#fff" stroke-width="1.7"/></svg><span>2 dental implants</span></li>
      <li><svg class="ico" viewBox="0 0 14 14"><circle cx="7" cy="7" r="7" fill="var(--teal-dark)"/><path d="M3.8 7.2 L6.1 9.4 L10.3 4.9" fill="none" stroke="#fff" stroke-width="1.7"/></svg><span>A brand new custom overdenture</span></li>
    </ul>
    <p class="abs excl">Does not include sedation or<br>extractions (if needed)</p>
  </section>

  <div class="abs clinician" role="img" aria-label="Photo of the implant clinician in dark scrubs, arms crossed"></div>

  <div class="abs cta">
    <span class="cta-label">Book a Free Consultation</span>
    <span class="cta-phone"><svg width="18" height="18" viewBox="0 0 24 24"><path d="M6.6 10.8a15.1 15.1 0 0 0 6.6 6.6l2.2-2.2a1 1 0 0 1 1-.25 11.4 11.4 0 0 0 3.6.57 1 1 0 0 1 1 1V20a1 1 0 0 1-1 1A17 17 0 0 1 3 4a1 1 0 0 1 1-1h3.5a1 1 0 0 1 1 1c0 1.25.2 2.45.57 3.57a1 1 0 0 1-.25 1z" fill="var(--teal)"/></svg>08 5127 3046</span>
  </div>
  <p class="abs footer">www.brolvenclinic.com.au<span class="sep">|</span>Located near Tallowmere shopping centre</p>
</main>
</body>
</html>
```